Larkmont Business Card Design Project

Double side card , just the logo on oxford white background on one side , and the rest of the information on the other side..
the company name is : Larkmont International General Trading LLC.
logo is already attached
the card to show in the info side: company name, employee name and position (job title) phone number, fax number, email address, P.O. box, Location (city and country)
deadline is already extended 4 all to have more time... thanks

```html
<!DOCTYPE html>
<html lang="en">
<head>
<meta charset="utf-8">
<title>Larkmont International General Trading LLC – Business Card</title>
<link rel="stylesheet" href="https://fonts.googleapis.com/css2?family=Montserrat:wght@400;700;800&display=swap">
<style>
  :root {
    --backdrop: #2e2c2c;
    --brand-cyan: #14bfe0;
    --card-white: #ffffff;
    --oxford-white: #fbfbf8;
  }
  * { box-sizing: border-box; margin: 0; padding: 0; }
  html, body { width: 1200px; height: 893px; overflow: hidden; }
  body {
    background: var(--backdrop);
    font-family: "Montserrat", Arial, sans-serif;
    display: flex;
    flex-direction: column;
    align-items: center;
    justify-content: center;
    gap: 60px;
  }
  .card {
    position: relative;
    width: 600px;
    height: 343px;
    overflow: hidden;
  }

  /* Logo side */
  .card--logo { background: var(--oxford-white); }
  .logo-ring {
    position: absolute;
    left: 50%; top: 50%;
    width: 210px; height: 210px;
    transform: translate(-50%, -50%);
    border: 9px solid var(--brand-cyan);
    border-radius: 50%;
    display: flex;
    align-items: center;
    justify-content: center;
  }
  .logo-placeholder {
    color: var(--brand-cyan);
    font-weight: 800;
    font-size: 34px;
    line-height: 0.9;
    text-align: center;
  }

  /* Info side */
  .card--info { background: var(--brand-cyan); color: var(--card-white); }
  .company-name {
    position: absolute;
    left: 18px; top: 16px;
    font-weight: 800;
    font-size: 30px;
    line-height: 0.88;
    letter-spacing: 0.5px;
    text-transform: uppercase;
  }
  .divider {
    position: absolute;
    left: 16px; top: 130px;
    width: 380px; height: 3px;
    background: var(--card-white);
  }
  .employee {
    position: absolute;
    left: 18px; top: 138px;
  }
  .employee-name {
    font-weight: 800;
    font-size: 15px;
    letter-spacing: 0.4px;
    line-height: 1;
  }
  .employee-title {
    font-weight: 400;
    font-size: 11px;
    line-height: 1.1;
  }
  .logo-disc {
    position: absolute;
    left: 388px; top: 108px;
    width: 124px; height: 124px;
    border-radius: 50%;
    background: var(--card-white);
    display: flex;
    align-items: center;
    justify-content: center;
  }
  .logo-disc .logo-placeholder { font-size: 24px; }
  .contact {
    position: absolute;
    left: 26px; top: 212px;
    font-size: 12.5px;
    line-height: 1.3;
    list-style: none;
  }
  .address {
    position: absolute;
    right: 22px; bottom: 22px;
    font-size: 12.5px;
    line-height: 1.3;
    text-align: right;
    font-style: normal;
  }
</style>
</head>
<body>
  <section class="card card--logo" aria-label="Logo side">
    <div class="logo-ring">
      <p class="logo-placeholder">LOGO<br>HERE</p>
    </div>
  </section>

  <section class="card card--info" aria-label="Information side">
    <h1 class="company-name">Larkmont<br>International<br>General<br>Trading LLC</h1>
    <div class="divider"></div>
    <div class="employee">
      <p class="employee-name">JOHN DOE SMITH</p>
      <p class="employee-title">Job Title Senior Editor</p>
    </div>
    <div class="logo-disc">
      <p class="logo-placeholder">LOGO<br>HERE</p>
    </div>
    <ul class="contact">
      <li>Sample phone number</li>
      <li>Sample Fax Number</li>
      <li>sample.email@larkmont.example</li>
    </ul>
    <address class="address">Sample P.O. box,<br>Location (city and country)</address>
  </section>
</body>
</html>
```